HollowPine Ventures Inc. Business Card Design

My business is custom renovations and homes.I would need to have a new business logo created to go along with my company name. The business card should be of a modern style as this is the market I am focused on. I would need my contact information and website posted on the card. I would also like to list a few of the tasks I conduct on the card (such as: Renovations, Additions, Repairs, New Homes, Design, Consultations). On the reverse of the card I currently have just my logo and my motto, "Shaping A Bold Path". However, I am open to completely changing everything as I am starting a new year and would like to excel further. Any new ideas and suggestions are always welcomed. Thank you.

Target Market(s)

Upscale residential and commercial renovations and builds

Industry/Entity Type

Business

Contact Information for Business Card

I would like the design to be able to be laser cut or burnt onto a wooden business card. I will be creating one option of cards for really loyal customers (wooden) and a second option for the everyday customer (paper).

Font styles to use
Other font styles liked:
• Calibri / anything of mordern taste

Colors
f37122
5c5c5c
474747
ffffff

Requirements
Must have
• I would like the colours of my business to be a sharp orange and grey. I believe this will symbolize a modern style. I am open to other suggestions if this is not suitable for the designers tastes. My contact info as follows:
• Will Marsh
• President
• HollowPine Ventures Inc.
• 555-214-3987
• will@hollowpineventures.example
• I would like my website (currently under construction) hollowpineventures.example on the card aswell.
Nice to have
• Along with a modern logo representing HollowPine, I would like something on the card besides the logo and contact information. Perhaps a small background design. I feel it may be nice to have my services listed on the card (in smaller font on the bottom) Renovations, Additions, Repairs, Design, Consultations.
Should not have
• The business card should not have too many different colors. Should not have rounded corners.

```html
<!DOCTYPE html>
<html lang="en">
<head>
<meta charset="utf-8">
<title>HollowPine Ventures Inc. Business Card</title>
<link rel="stylesheet" href="https://fonts.googleapis.com/css2?family=Open+Sans:wght@400;600;700&display=swap">
<style>
  :root {
    --orange: #f37122;
    --grey-mid: #5c5c5c;
    --grey-dark: #474747;
    --white: #ffffff;
    --backdrop: #b8b8b8;
    --wood-dark: #1c1c1c;
    --wood-light: #333333;
  }
  * { box-sizing: border-box; margin: 0; padding: 0; }
  html, body { width: 1200px; height: 837px; overflow: hidden; }
  body {
    background: var(--backdrop);
    font-family: "Open Sans", sans-serif;
    position: relative;
  }
  .card {
    position: absolute;
    top: 270px;
    width: 525px;
    height: 300px;
    box-shadow: 0 10px 24px rgba(0,0,0,0.22);
    overflow: hidden;
  }
  /* Front */
  .card-front { left: 45px; }
  .card-front .wood {
    position: absolute; inset: 0;
    background: linear-gradient(135deg, var(--wood-light), var(--wood-dark) 55%, #262626);
  }
  .front-content {
    position: absolute; inset: 0;
    display: flex; flex-direction: column; align-items: center; justify-content: center;
    color: var(--white);
    text-align: center;
  }
  .front-mark {
    font-size: 54px; font-weight: 700; color: var(--orange);
    line-height: 1; margin-bottom: 14px;
  }
  .company-name {
    font-size: 30px; font-weight: 600; color: var(--white); line-height: 1.1;
  }
  .tagline {
    font-size: 14px; letter-spacing: 5px; margin-top: 6px; color: var(--white);
  }
  .services {
    position: absolute; left: 0; right: 0; bottom: 30px;
    text-align: center; font-size: 14px; font-weight: 600; color: var(--white);
  }
  .services .sep { color: var(--orange); margin: 0 6px; }

  /* Back */
  .card-back { left: 630px; background: var(--white); }
  .back-layout {
    position: absolute; inset: 0;
    display: flex; align-items: center;
  }
  .back-mark {
    width: 245px; text-align: center;
    font-size: 40px; font-weight: 700; color: var(--orange);
  }
  .divider {
    width: 1px; height: 120px; background: var(--grey-mid);
  }
  .contact { padding-left: 28px; }
  .person-name { font-size: 22px; font-weight: 700; color: var(--grey-dark); line-height: 1.1; }
  .person-title { font-size: 14px; color: var(--orange); margin-bottom: 14px; }
  .contact-row {
    display: flex; align-items: center; gap: 7px;
    font-size: 13px; color: var(--grey-dark); line-height: 1.5;
  }
  .contact-row svg { flex: none; }
  .website { font-size: 14px; color: var(--orange); margin-top: 6px; }
</style>
</head>
<body>

<section class="card card-front">
  <div class="wood" role="img" aria-label="Dark stained wood plank texture background"></div>
  <div class="front-content">
    <div class="front-mark">HollowPine</div>
    <div class="company-name">HollowPine Ventures Inc.</div>
    <div class="tagline">Shaping A Bold Path</div>
  </div>
  <div class="services">
    Renovations<span class="sep">|</span>Additions<span class="sep">|</span>Repairs<span class="sep">|</span>Design<span class="sep">|</span>Consultations
  </div>
</section>

<section class="card card-back">
  <div class="back-layout">
    <div class="back-mark">HollowPine</div>
    <div class="divider"></div>
    <div class="contact">
      <div class="person-name">Will Marsh</div>
      <div class="person-title">President</div>
      <div class="contact-row">
        <svg width="14" height="14" viewBox="0 0 14 14" aria-hidden="true">
          <rect width="14" height="14" fill="var(--orange)"/>
          <path d="M4 3 L6 3 L6.5 5 L5.5 6 Q6.5 8 8 8.5 L9 7.5 L11 8 L11 10 Q6 11 3.5 4.5 Z" fill="var(--white)"/>
        </svg>
        <span>555-214-3987</span>
      </div>
      <div class="contact-row">
        <svg width="14" height="14" viewBox="0 0 14 14" aria-hidden="true">
          <rect width="14" height="14" fill="var(--orange)"/>
          <rect x="3" y="4" width="8" height="6" fill="none" stroke="var(--white)" stroke-width="1"/>
          <path d="M3 4 L7 7.5 L11 4" fill="none" stroke="var(--white)" stroke-width="1"/>
        </svg>
        <span>will@hollowpineventures.example</span>
      </div>
      <div class="website">hollowpineventures.example</div>
    </div>
  </div>
</section>

</body>
</html>
```